Stationary design for IT Consultancy
Stationary Design (Business Cards - Letter Heads - Envelopes - Presentation Folders - Power Point)
Stationary design for IT Consultancy - Information Technology
Creative Brief
Use standard fonts
Optional fonts can be used
Professional
Dean Marlow
Technical Director
14 Brindle Works Oakfield Lane Stoneham Wexshire WX7 2QP
dean.marlow@pivotal-nsg.net
www.pivotal-nsg.net

```html
<!DOCTYPE html>
<html lang="en">
<head>
<meta charset="utf-8">
<title>Pivotal Network Systems Group — Stationery</title>
<link rel="stylesheet" href="https://fonts.googleapis.com/css2?family=Montserrat:wght@400;600;700&display=swap">
<style>
  :root{
    --brand-blue:#4060b4;
    --brand-blue-dark:#34519f;
    --paper:#ffffff;
    --backdrop:#ececec;
    --ink:#55596a;
    --faint:#eef1f8;
  }
  *{box-sizing:border-box;margin:0;padding:0}
  html,body{width:1200px;height:936px;overflow:hidden}
  body{background:radial-gradient(circle at 50% 40%,#f7f7f7,var(--backdrop));font-family:"Montserrat",Arial,sans-serif;color:var(--ink);position:relative}
  .sheet{position:absolute;background:var(--paper);box-shadow:0 2px 6px rgba(0,0,0,.18);overflow:hidden}
  .sheet svg.shape{position:absolute;inset:0;width:100%;height:100%}
  .wordmark{position:absolute;font-weight:700;color:var(--brand-blue);line-height:1;letter-spacing:.06em}
  .wordmark .mark-dot{display:inline-block;border-radius:50%;background:var(--brand-blue);vertical-align:middle;margin-right:.35em}
  .wordmark small{display:block;font-size:.42em;letter-spacing:.22em;margin-top:.35em}
  .small-text{position:absolute;font-size:6px;line-height:1.55;color:var(--ink)}

  .letterhead{left:173px;top:36px;width:413px;height:583px}
  .letterhead .wordmark{left:20px;top:34px;font-size:13px}
  .letterhead .wordmark .mark-dot{width:10px;height:10px}
  .letterhead .small-text{left:20px;bottom:26px}

  .folder{left:637px;top:36px;width:464px;height:583px}
  .folder .wordmark{left:0;right:0;top:290px;text-align:center;font-size:38px}
  .folder .wordmark .mark-dot{width:24px;height:24px}
  .folder .wordmark small{font-size:13px;margin-top:8px}

  .card-front{left:43px;top:657px;width:199px;height:97px}
  .card-front .wordmark{left:10px;top:14px;font-size:9px}
  .card-front .wordmark .mark-dot{width:7px;height:7px}
  .card-front .small-text{right:10px;bottom:8px;text-align:right;font-size:5px}
  .card-front .person{font-weight:700;font-size:6px;color:var(--brand-blue)}

  .card-back{left:43px;top:772px;width:199px;height:102px;background:var(--brand-blue)}
  .card-back .web{position:absolute;left:0;right:0;bottom:10px;text-align:center;font-size:5.5px;letter-spacing:.2em;color:#fff}

  .envelope-front{left:268px;top:670px;width:433px;height:214px}
  .envelope-front .wordmark{left:16px;top:22px;font-size:11px}
  .envelope-front .wordmark .mark-dot{width:9px;height:9px}
  .envelope-front .small-text{left:16px;top:56px;font-size:5px}

  .envelope-back{left:741px;top:670px;width:431px;height:214px}
  .envelope-back .web{position:absolute;left:0;right:0;top:28px;text-align:center;font-size:8px;letter-spacing:.32em;color:#fff;font-weight:600}
</style>
</head>
<body>

<section class="sheet letterhead" aria-label="Letterhead">
  <svg class="shape" viewBox="0 0 413 583" aria-hidden="true">
    <path d="M150 0H413V175Q330 40 150 0Z" fill="var(--brand-blue)"/>
    <path d="M18 20Q310 45 413 195" fill="none" stroke="var(--brand-blue)" stroke-width="2"/>
    <circle cx="160" cy="330" r="80" fill="var(--faint)"/>
  </svg>
  <div class="wordmark"><span class="mark-dot"></span>PIVOTAL<small>NETWORK SYSTEMS GROUP</small></div>
  <p class="small-text">14 Brindle Works, Oakfield Lane<br>Stoneham, Wexshire WX7 2QP<br>T: 01632 960418<br>dean.marlow@pivotal-nsg.net<br>www.pivotal-nsg.net</p>
</section>

<section class="sheet folder" aria-label="Presentation folder">
  <svg class="shape" viewBox="0 0 464 583" aria-hidden="true">
    <path d="M0 0H464V200Q330 40 0 28Z" fill="var(--brand-blue)"/>
    <path d="M0 42Q330 55 464 215" fill="none" stroke="var(--brand-blue)" stroke-width="2"/>
  </svg>
  <div class="wordmark"><span class="mark-dot"></span>PIVOTAL<small>NETWORK SYSTEMS GROUP</small></div>
</section>

<section class="sheet card-front" aria-label="Business card front">
  <svg class="shape" viewBox="0 0 199 97" aria-hidden="true">
    <path d="M90 0H199V40Q160 8 90 0Z" fill="var(--brand-blue)"/>
    <path d="M70 3Q165 12 199 46" fill="none" stroke="var(--brand-blue)" stroke-width="1"/>
  </svg>
  <div class="wordmark"><span class="mark-dot"></span>PIVOTAL<small>NETWORK SYSTEMS GROUP</small></div>
  <p class="small-text"><span class="person">Dean Marlow</span><br>Technical Director<br>T: 01632 960418<br>dean.marlow@pivotal-nsg.net</p>
</section>

<section class="sheet card-back" aria-label="Business card back">
  <svg class="shape" viewBox="0 0 199 102" aria-hidden="true">
    <circle cx="70" cy="48" r="30" fill="#ffffff" fill-opacity=".12"/>
    <path d="M0 0H199V6Q100 30 0 14Z" fill="#ffffff" fill-opacity=".9"/>
  </svg>
  <p class="web">WWW.PIVOTAL-NSG.NET</p>
</section>

<section class="sheet envelope-front" aria-label="Envelope front">
  <svg class="shape" viewBox="0 0 433 214" aria-hidden="true">
    <path d="M180 0H433V85Q340 15 180 0Z" fill="var(--brand-blue)"/>
    <path d="M130 4Q350 25 433 95" fill="none" stroke="var(--brand-blue)" stroke-width="1.5"/>
  </svg>
  <div class="wordmark"><span class="mark-dot"></span>PIVOTAL<small>NETWORK SYSTEMS GROUP</small></div>
  <p class="small-text">14 Brindle Works, Oakfield Lane<br>Stoneham, Wexshire WX7 2QP</p>
</section>

<section class="sheet envelope-back" aria-label="Envelope back">
  <svg class="shape" viewBox="0 0 431 214" aria-hidden="true">
    <path d="M0 0H431V62Q215 95 0 62Z" fill="var(--brand-blue)"/>
    <path d="M0 70Q215 104 431 70" fill="none" stroke="var(--brand-blue)" stroke-width="1" stroke-opacity=".5"/>
  </svg>
  <p class="web">WWW.PIVOTAL-NSG.NET</p>
</section>

</body>
</html>
```